Professional/modern business card design for construction company

We need a new business card design, double sided keeping it modern, sleek, professional and simple. We are an earthmoving business but do not want any pictures of machinery. I would like one side to have the logo and the other to have all the information, keeping with the colors in our logo. The business card will need to be able to be customised so we can use it for several different managers., we would also like to be able to use the design to apply it to other stationary ie. letterheads, notebooks etc. We do not really have a tag line but we could put on there that we specialise in - Agriculture, Civil Construction and Mining.

Contact Information for Business Card

Brolga Ridge Excavations Pty Ltd
ABN 58 402 937 615
82 Gumleaf Creek Road, Moree NSW 2400

Harold Benton
Managing Director
P 0418 639 204
E haroldbenton@brolgaridgeexc.com.au

Font styles to use
Serif
Sans Serif

Requirements
Nice to have
• I have attached some examples of ideas.
Should not have
• images of machinery

```html
<!DOCTYPE html>
<html lang="en">
<head>
<meta charset="utf-8">
<title>Brolga Ridge Excavations – Business Card</title>
<link rel="stylesheet" href="https://fonts.googleapis.com/css2?family=Montserrat:wght@300;400;500;700&family=Didact+Gothic&display=swap">
<style>
  :root {
    --stage: #2b2e33;
    --card-black: #0c0c0d;
    --orange: #f58220;
    --orange-light: #f7a11f;
    --white: #f4f4f4;
    --ink: #141414;
    --grey: #5b5b5b;
  }
  * { margin: 0; padding: 0; box-sizing: border-box; }
  html, body {
    width: 1200px; height: 900px; overflow: hidden;
    background: var(--stage);
  }
  .stage {
    width: 1200px; height: 900px;
    display: flex; flex-direction: column;
    align-items: center; justify-content: center;
    gap: 56px;
  }
  .card {
    width: 630px; height: 360px;
    position: relative;
    border-radius: 3px;
    box-shadow: 0 14px 30px rgba(0,0,0,0.45);
  }

  /* Logo side */
  .card--brand {
    background: var(--card-black);
    display: flex; flex-direction: column;
    align-items: center; justify-content: center;
    gap: 22px;
  }
  .brand-mark {
    display: flex; align-items: center; gap: 14px;
  }
  .brand-mark__square {
    width: 22px; height: 22px; background: var(--orange);
  }
  .brand-mark__name {
    font-family: "Montserrat", sans-serif;
    font-weight: 700;
    font-size: 25px;
    letter-spacing: 0.5px;
    color: var(--orange);
    text-transform: uppercase;
  }
  .brand-tagline {
    font-family: "Didact Gothic", sans-serif;
    font-size: 21px;
    color: var(--grey);
    letter-spacing: 0.4px;
  }

  /* Contact side */
  .card--contact {
    background: linear-gradient(225deg, var(--orange-light) 0%, var(--orange) 70%);
    font-family: "Montserrat", sans-serif;
    text-align: right;
    padding: 48px 44px 40px 40px;
    display: flex; flex-direction: column; justify-content: space-between;
  }
  .person__name {
    font-size: 34px; color: var(--white); line-height: 1.1;
  }
  .person__first { font-weight: 700; }
  .person__last { font-weight: 300; }
  .person__role {
    margin-top: 4px;
    font-size: 17px; font-weight: 400;
    color: var(--white); letter-spacing: 0.6px;
  }
  .details {
    list-style: none;
    font-size: 16px; font-weight: 400;
    color: var(--ink); line-height: 1.5;
  }
</style>
</head>
<body>
<main class="stage">
  <section class="card card--brand" aria-label="Business card, logo side">
    <div class="brand-mark">
      <span class="brand-mark__square"></span>
      <span class="brand-mark__name">Brolga Ridge Excavations Pty Ltd</span>
    </div>
    <p class="brand-tagline">Agriculture, Civil Construction and Mining</p>
  </section>

  <section class="card card--contact" aria-label="Business card, contact side">
    <div class="person">
      <h1 class="person__name"><span class="person__first">Harold</span> <span class="person__last">Benton</span></h1>
      <p class="person__role">Managing Director</p>
    </div>
    <ul class="details">
      <li class="details__phone">0418 639 204</li>
      <li class="details__email">haroldbenton@brolgaridgeexc.com.au</li>
      <li class="details__abn">ABN 58 402 937 615</li>
      <li class="details__address">82 Gumleaf Creek Road, Moree NSW 2400</li>
    </ul>
  </section>
</main>
</body>
</html>
```